チラシは対象のお子様の親に見て頂きます。(1番)
地域の保健師・相談員(このようなサービスを紹介する人)や保育所等の先生にも見られると思います。
こちらで作ったものをアレンジして頂きたいと思います。
全て使用しなくでも大丈夫です。
写真を使用していきたいのですが、いま題材がないので、ネットのサンプル画像を利用して頂けると幸いです。どのような写真があればいいか教えて頂ければ、弊社での撮影も可能です。
A4
片面
• 高解像度JPG (.jpg)
• イラストレーター形式 (.ai)

```html
<!DOCTYPE html>
<html lang="ja">
<head>
<meta charset="utf-8">
<title>保育所等訪問支援</title>
<link rel="stylesheet" href="https://fonts.googleapis.com/css2?family=M+PLUS+Rounded+1c:wght@400;500;700;800&display=swap">
<style>
:root{
  --orange:#ef8a2c;
  --orange-deep:#e0701a;
  --orange-soft:#f6b46a;
  --cream:#fdf3e4;
  --cream-2:#fbe6c8;
  --ink:#4a3a2c;
  --muted:#7a6a5a;
  --white:#ffffff;
}
*{box-sizing:border-box;margin:0;padding:0}
html,body{width:849px;height:1200px;overflow:hidden}
body{font-family:"M PLUS Rounded 1c",sans-serif;color:var(--ink);background:var(--white)}
.flyer{position:relative;width:849px;height:1200px;background:var(--cream);overflow:hidden}

.hero{position:absolute;left:0;top:0;width:849px;height:470px;background:linear-gradient(180deg,#fff8ee 0%,var(--cream) 100%)}
.hero-figure{position:absolute;left:300px;top:40px;width:230px;height:280px;border-radius:110px 110px 20px 20px;background:linear-gradient(180deg,#f7d6a8,#f3c07e)}
.bubble{position:absolute;border-radius:50%;background:var(--white);border:2px solid var(--orange-soft);display:flex;align-items:center;justify-content:center;text-align:center;font-size:14px;font-weight:500;line-height:1.4;color:var(--ink)}
.bubble.b1{left:135px;top:78px;width:150px;height:100px}
.bubble.b2{left:70px;top:172px;width:108px;height:96px}
.bubble.b3{left:560px;top:40px;width:110px;height:82px}
.bubble.b4{left:640px;top:110px;width:122px;height:96px}

.title-sub{position:absolute;left:0;top:322px;width:849px;text-align:center;font-size:46px;font-weight:800;color:var(--orange);letter-spacing:2px}
.title-main{position:absolute;left:0;top:380px;width:849px;text-align:center;font-size:74px;font-weight:800;color:var(--orange-deep);letter-spacing:4px}
.lead{position:absolute;left:0;top:470px;width:849px;text-align:center;font-size:14px;font-weight:500;line-height:1.6;color:var(--ink)}

.about-label{position:absolute;left:285px;top:520px;width:200px;height:24px;border-radius:12px;background:var(--orange);color:var(--white);font-size:13px;font-weight:700;text-align:center;line-height:24px}
.about-text{position:absolute;left:50px;top:555px;width:390px;font-size:11.5px;line-height:1.75;color:var(--ink)}
.photo{position:absolute;border-radius:8px;background:linear-gradient(135deg,#f4d9b8,#e9c190)}
.photo.p1{left:455px;top:548px;width:170px;height:135px}
.photo.p2{left:635px;top:522px;width:170px;height:95px}
.photo.p3{left:635px;top:625px;width:170px;height:58px}

.facts{position:absolute;left:40px;top:705px;width:769px;display:flex;gap:10px}
.fact{flex:1;background:var(--white);border:2px solid var(--orange-soft);border-radius:8px;padding:24px 10px 10px;position:relative;height:125px}
.fact-tag{position:absolute;left:50%;top:-12px;transform:translateX(-50%);background:var(--orange);color:var(--white);font-size:12px;font-weight:700;padding:2px 16px;border-radius:10px;white-space:nowrap}
.fact p{font-size:11px;line-height:1.6;color:var(--ink)}

.flow{position:absolute;left:20px;top:848px;width:809px;height:205px;background:var(--orange);border-radius:10px}
.flow-title{position:absolute;left:0;top:8px;width:100%;text-align:center;color:var(--white);font-size:15px;font-weight:700}
.flow-steps{position:absolute;left:10px;top:40px;display:flex;align-items:center;gap:5px}
.step{width:148px;height:150px;background:var(--white);border-radius:6px;padding:10px}
.step h3{font-size:13px;font-weight:700;color:var(--orange-deep);margin-bottom:6px}
.step p{font-size:10.5px;line-height:1.6}
.arrow{width:14px;height:24px;flex:none}
.flow-end{width:100px;height:150px;background:var(--white);border-radius:6px;color:var(--orange-deep);font-size:15px;font-weight:700;display:flex;align-items:center;justify-content:center;text-align:center;line-height:1.5}

.footer{position:absolute;left:0;top:1068px;width:849px;height:132px;background:var(--white)}
.brand{position:absolute;left:50px;top:14px;display:flex;align-items:center;gap:10px}
.brand-dot{width:36px;height:36px;border-radius:50%;background:var(--orange-soft)}
.brand-name{font-size:24px;font-weight:700;color:var(--muted)}
.brand-en{position:absolute;left:96px;top:50px;font-size:11px;color:var(--muted);letter-spacing:1px}
.phone{position:absolute;left:50px;top:72px;display:flex;align-items:center;gap:6px;font-size:30px;font-weight:800;color:var(--orange-deep)}
.hours{position:absolute;left:50px;top:112px;font-size:10px;color:var(--muted)}
.address{position:absolute;left:340px;top:72px;font-size:11px;line-height:1.6;color:var(--ink)}
.map{position:absolute;left:560px;top:14px;width:250px;height:108px;background:linear-gradient(135deg,#f3eee6,#e6ddd0);border-radius:4px}
</style>
</head>
<body>
<div class="flyer">
  <section class="hero">
    <div class="hero-figure" role="img" aria-label="手を挙げて話す保育スタッフのイラスト"></div>
    <div class="bubble b1">活動に集中できず、<br>参加が難しい</div>
    <div class="bubble b2">お友達と<br>なかなか<br>遊べない</div>
    <div class="bubble b3">行事への<br>参加が難しい</div>
    <div class="bubble b4">勉強が苦手で<br>ついていけない</div>
  </section>

  <h2 class="title-sub">子供のやってみようを叶える</h2>
  <h1 class="title-main">保育所等訪問支援</h1>
  <p class="lead">集団での生活の困りごとについて、集団生活の中で過ごしやすく<br>なるように、助言して一緒に考えさせて頂きます。</p>

  <div class="about-label">保育所等訪問支援とは</div>
  <div class="about-text">
    <p>◎保育所等訪問支援とは、お子さんが通う保育所や学校などに専門スタッフが訪問し、集団生活に適応できるよう支援するサービスです。</p>
    <p>◎お子さんへの直接の支援に加え、先生方へ関わり方の助言を行い、園や学校での過ごしやすさを一緒に考えます。</p>
    <p>◎保護者の方と園・学校をつなぎ、情報を共有しながら継続的に支援を行います。</p>
  </div>
  <div class="photo p1" role="img" aria-label="保育室で遊ぶ子どもたちの写真"></div>
  <div class="photo p2" role="img" aria-label="先生と子どもが一緒に活動する写真"></div>
  <div class="photo p3" role="img" aria-label="子どもの手元の写真"></div>

  <div class="facts">
    <div class="fact"><span class="fact-tag">対象</span><p>保育所、幼稚園、認定こども園、小学校、特別支援学校などに通う、支援が必要なお子さん</p></div>
    <div class="fact"><span class="fact-tag">頻度</span><p>月1回から2回程度<br>お子さんの状況に合わせて訪問します</p></div>
    <div class="fact"><span class="fact-tag">利用料金</span><p>世帯の所得に応じて上限額があります。詳しくはお問い合わせください</p></div>
    <div class="fact"><span class="fact-tag">情報共有</span><p>訪問後は保護者の方へ様子を報告し、今後の支援について相談します</p></div>
  </div>

  <section class="flow">
    <div class="flow-title">ご利用の流れ</div>
    <div class="flow-steps">
      <div class="step"><h3>相談</h3><p>まずはお電話でご相談ください。ご家庭の困りごとをお聞きします。</p></div>
      <svg class="arrow" viewBox="0 0 14 24"><path d="M2 2 L12 12 L2 22" fill="none" stroke="#fff" stroke-width="3"/></svg>
      <div class="step"><h3>見学・体験</h3><p>事業所の見学や面談を行い、支援内容についてご説明します。</p></div>
      <svg class="arrow" viewBox="0 0 14 24"><path d="M2 2 L12 12 L2 22" fill="none" stroke="#fff" stroke-width="3"/></svg>
      <div class="step"><h3>受給者証の申請</h3><p>お住まいの市町村で受給者証の申請手続きを行います。</p></div>
      <svg class="arrow" viewBox="0 0 14 24"><path d="M2 2 L12 12 L2 22" fill="none" stroke="#fff" stroke-width="3"/></svg>
      <div class="step"><h3>契約・計画作成</h3><p>ご契約のうえ、個別支援計画を作成し訪問を始めます。</p></div>
      <svg class="arrow" viewBox="0 0 14 24"><path d="M2 2 L12 12 L2 22" fill="none" stroke="#fff" stroke-width="3"/></svg>
      <div class="flow-end">サービスの<br>開始</div>
    </div>
  </section>

  <footer class="footer">
    <div class="brand"><span class="brand-dot"></span><span class="brand-name">こどもデイサービス ひだまり</span></div>
    <div class="brand-en">kodomo day service hidamari</div>
    <div class="phone">
      <svg width="26" height="26" viewBox="0 0 24 24"><path d="M6.6 10.8a15 15 0 0 0 6.6 6.6l2.2-2.2c.3-.3.7-.4 1-.2 1.1.4 2.3.6 3.6.6.6 0 1 .4 1 1V20c0 .6-.4 1-1 1A17 17 0 0 1 3 4c0-.6.4-1 1-1h3.5c.6 0 1 .4 1 1 0 1.3.2 2.5.6 3.6.1.3 0 .7-.2 1z" fill="#e0701a"/></svg>
      0948-00-1234
    </div>
    <div class="hours">営業時間 9:30〜17:30　相談時間 10:00〜16:00　定休日 日曜・祝日</div>
    <div class="address">〒820-0000 架空市中央1-2-3<br>FAX 0948-00-1235</div>
    <div class="map" role="img" aria-label="事業所周辺の地図"></div>
  </footer>
</div>
</body>
</html>
```